Circus Poster 2016

We want to revise our circus poster for our 2016 tour. We very much liked the poster we used last year (attached) and want to stay with this colour scheme and with this logo. However, we want to enhance the family friendliness of the poster, so perhaps the addition of a family having a great time would be a good idea.

The winner will be paid to modify this poster for each of the 30 events we are doing this year plus making a flyer (based on the poster design). So the winner of this contest gets a job for a year.

Circus

```html
<!DOCTYPE html>
<html lang="en">
<head>
<meta charset="utf-8">
<title>Marlowe's Circus – July Offer 2016</title>
<link rel="stylesheet" href="https://fonts.googleapis.com/css2?family=Oswald:wght@500;700&family=Luckiest+Guy&family=Archivo+Narrow:wght@700&display=swap">
<style>
  :root {
    --paper: #ffffff;
    --sun: #ecf40f;
    --circus-red: #a8121b;
    --bright-red: #d8262c;
    --ink: #111111;
    --skin: #e9c7ae;
  }
  * { margin: 0; padding: 0; box-sizing: border-box; }
  html, body { width: 862px; height: 1200px; overflow: hidden; background: var(--paper); }
  .poster {
    position: relative;
    width: 862px; height: 1200px;
    background: var(--paper);
    overflow: hidden;
  }
  .field {
    position: absolute; left: 14px; top: 14px; width: 834px; height: 1168px;
    background: var(--sun);
  }
  .frame {
    position: absolute; left: 42px; top: 52px; width: 780px; height: 860px;
    border: 3px solid var(--circus-red);
  }
  .brand {
    position: absolute; left: 60px; top: 22px; width: 742px;
    text-align: center;
    font-family: "Oswald", sans-serif; font-weight: 700;
    color: var(--bright-red);
    background: var(--sun);
    line-height: 1;
  }
  .brand__possessive { display: block; font-size: 58px; letter-spacing: 2px; }
  .brand__name { display: block; font-size: 132px; letter-spacing: 4px; margin-top: 2px; }
  .hero-photo {
    position: absolute; left: 14px; top: 262px; width: 834px; height: 704px;
    border-radius: 260px 260px 0 0;
    background:
      radial-gradient(ellipse 30% 34% at 52% 40%, var(--skin) 0%, #e2b49a 60%, rgba(226,180,154,0) 100%),
      radial-gradient(ellipse 40% 22% at 50% 12%, #7d1016 0%, rgba(125,16,22,0) 100%),
      linear-gradient(180deg, #b52a2f 0%, #c2373b 55%, #9c1a20 100%);
  }
  .family-photo {
    position: absolute; left: 40px; top: 500px; width: 290px; height: 240px;
    border: 6px solid var(--sun);
    border-radius: 18px;
    background:
      radial-gradient(ellipse 60% 50% at 50% 40%, #f2cfb4 0%, rgba(242,207,180,0) 100%),
      linear-gradient(160deg, #4d7fc4 0%, #e0a23a 100%);
    transform: rotate(-4deg);
  }
  .offer-badge {
    position: absolute; left: 562px; top: 323px; width: 246px; height: 246px;
    border-radius: 50%;
    background: var(--circus-red);
    border: 7px solid var(--sun);
    display: flex; flex-direction: column; align-items: center; justify-content: center;
    font-family: "Luckiest Guy", "Oswald", sans-serif; color: var(--sun);
    font-size: 60px; line-height: 1;
    transform: rotate(-12deg);
  }
  .promo {
    position: absolute; left: 88px; top: 770px; width: 680px; height: 120px;
    transform: rotate(-3deg);
  }
  .promo__shadow {
    position: absolute; inset: 0; background: var(--ink);
    transform: translate(8px, -12px) skewX(-4deg);
  }
  .promo__strip {
    position: absolute; inset: 0; background: var(--sun);
    display: flex; align-items: center; justify-content: center;
    font-family: "Luckiest Guy", "Oswald", sans-serif; font-size: 78px; color: var(--ink);
    letter-spacing: 1px; padding-top: 8px; white-space: nowrap;
  }
  .terms {
    position: absolute; left: 14px; top: 918px; width: 834px;
    text-align: center; font-family: "Oswald", sans-serif; font-weight: 500;
    font-style: italic; font-size: 17px; color: var(--paper);
    text-shadow: 0 1px 2px rgba(0,0,0,0.6);
  }
  .venue-band {
    position: absolute; left: 14px; top: 966px; width: 834px; height: 216px;
    background: var(--circus-red); color: var(--paper);
  }
  .venue {
    position: absolute; left: 44px; top: 12px;
    font-family: "Archivo Narrow", sans-serif; font-weight: 700; line-height: 1;
  }
  .venue__town { font-size: 74px; letter-spacing: 1px; }
  .venue__park { font-size: 34px; letter-spacing: 6px; margin-top: 6px; }
  .venue__street { font-size: 24px; letter-spacing: 2.5px; margin-top: 6px; }
  .divider {
    position: absolute; left: 482px; top: 24px; width: 2px; height: 134px; background: var(--paper);
  }
  .dates {
    position: absolute; left: 484px; top: 30px;
    font-family: "Archivo Narrow", sans-serif; font-weight: 700; color: var(--circus-red);
  }
  .dates span {
    display: block; background: var(--paper);
    height: 60px; line-height: 60px; padding-left: 42px; white-space: nowrap; overflow: hidden;
  }
  .dates__days { width: 318px; font-size: 52px; }
  .dates__year { width: 220px; font-size: 56px; margin-top: 4px; }
  .contact {
    position: absolute; left: 0; top: 168px; width: 834px;
    text-align: center; font-family: "Archivo Narrow", sans-serif; font-weight: 700;
    font-size: 34px; letter-spacing: 4px; white-space: nowrap;
  }
</style>
</head>
<body>
<main class="poster">
  <div class="field"></div>
  <div class="frame"></div>
  <div class="hero-photo" role="img" aria-label="Photograph of a smiling clown in a red bowler hat and striped red jacket holding a big-smile mask on a stick"></div>
  <div class="family-photo" role="img" aria-label="Photograph of a laughing family of parents and two children enjoying the circus show"></div>
  <h1 class="brand">
    <span class="brand__possessive">MARLOWE'S</span>
    <span class="brand__name">CIRCUS</span>
  </h1>
  <div class="offer-badge"><span>July</span><span>Offer</span></div>
  <div class="promo">
    <div class="promo__shadow"></div>
    <div class="promo__strip">KIDS GO FREE*</div>
  </div>
  <p class="terms">*One free kids ticket with every full-priced adult ticket purchased online or on the phone</p>
  <section class="venue-band">
    <div class="venue">
      <div class="venue__town">ASHBURY</div>
      <div class="venue__park">HAWTHORN PARK</div>
      <div class="venue__street">Kestrel road, HP00 1AB</div>
    </div>
    <div class="divider"></div>
    <div class="dates">
      <span class="dates__days">9-12 JULY</span>
      <span class="dates__year">2016</span>
    </div>
    <p class="contact">www.marlowescircus.com | 01632 555 250</p>
  </section>
</main>
</body>
</html>
```